Business card for STEADYWAVE

Please design professional business card for IT consulting firm STEADYWAVE INC.
Use logo attached.
Use information from sample qNode business card attached.
replace qnode inc with STEADYWAVE INC.
as well as qnodeinc.com with steadywave.example

```html
<!DOCTYPE html>
<html lang="en">
<head>
<meta charset="utf-8">
<title>STEADYWAVE Business Card</title>
<link rel="stylesheet" href="https://fonts.googleapis.com/css2?family=PT+Sans:wght@400;700&family=PT+Sans+Narrow:wght@700&display=swap">
<style>
  :root {
    --backdrop: #4f4f4f;
    --card-dark: #1a1a1a;
    --card-light: #ffffff;
    --ink: #1e1e1e;
    --brand-purple: #9a10d2;
    --brand-blue: #5cb9f4;
    --logo-white: #ffffff;
  }
  * { box-sizing: border-box; margin: 0; padding: 0; }
  html, body {
    width: 1200px; height: 1200px; overflow: hidden;
    background: var(--backdrop);
    font-family: "PT Sans", sans-serif;
  }
  .card {
    position: absolute;
    left: 241px;
    width: 727px;
    height: 436px;
  }
  .card--front { top: 114px; background: var(--card-dark); }
  .card--back { top: 635px; background: var(--card-light); color: var(--ink); }

  .wordmark {
    position: absolute;
    display: flex;
    align-items: center;
    font-family: "PT Sans", sans-serif;
    font-weight: 700;
    white-space: nowrap;
    line-height: 1;
  }
  .wordmark__square { display: block; background: var(--brand-purple); }

  .card--front .wordmark {
    left: 0; right: 0; top: 190px;
    justify-content: center;
    font-size: 58px;
    letter-spacing: 8px;
    color: var(--logo-white);
    gap: 10px;
  }
  .card--front .wordmark__square { width: 40px; height: 40px; }

  .card--back .wordmark {
    right: 48px; top: 62px;
    font-size: 42px;
    letter-spacing: 5px;
    color: #000;
    gap: 8px;
  }
  .card--back .wordmark__square { width: 30px; height: 30px; }

  .accent-bar {
    position: absolute; left: 0; top: 232px;
    width: 39px; height: 63px;
    background: var(--brand-blue);
  }
  .person { position: absolute; left: 48px; top: 226px; }
  .person__name {
    font-family: "PT Sans Narrow", sans-serif;
    font-weight: 700;
    font-size: 29px;
    line-height: 30px;
    letter-spacing: 0.2px;
  }
  .person__first { color: var(--brand-purple); }
  .person__last { color: var(--brand-blue); }
  .person__role { font-size: 16px; line-height: 19px; margin-top: 0; }

  .company { position: absolute; left: 417px; top: 226px; }
  .company__name {
    color: var(--brand-purple);
    font-weight: 700;
    font-size: 16.5px;
    line-height: 20px;
  }
  .company__address { font-size: 16.5px; line-height: 20px; }

  .contacts { list-style: none; margin-top: 13px; }
  .contacts li {
    display: flex; align-items: center;
    font-size: 16.5px; line-height: 22.5px;
  }
  .contacts svg {
    width: 13px; height: 13px; margin-right: 8px;
    fill: var(--brand-purple); flex: none;
  }
</style>
</head>
<body>

<section class="card card--front">
  <div class="wordmark">STEADYWAVE<span class="wordmark__square"></span></div>
</section>

<section class="card card--back">
  <div class="wordmark">STEADYWAVE<span class="wordmark__square"></span></div>

  <div class="accent-bar"></div>
  <div class="person">
    <p class="person__name"><span class="person__first">DANIEL</span> <span class="person__last">VORONOV</span></p>
    <p class="person__role">P. ENG.</p>
    <p class="person__role">General Manager</p>
  </div>

  <div class="company">
    <p class="company__name">STEADYWAVE INC.</p>
    <p class="company__address">1280 Harbor Line Rd., Suite 101</p>
    <p class="company__address">Fernvale, Ontario, L0X 1A0, Canada</p>

    <ul class="contacts">
      <li>
        <svg viewBox="0 0 24 24" aria-hidden="true"><path d="M6.6 10.8a15.1 15.1 0 0 0 6.6 6.6l2.2-2.2a1 1 0 0 1 1-.25 11.4 11.4 0 0 0 3.6.57 1 1 0 0 1 1 1V20a1 1 0 0 1-1 1A17 17 0 0 1 3 4a1 1 0 0 1 1-1h3.5a1 1 0 0 1 1 1c0 1.25.2 2.45.57 3.6a1 1 0 0 1-.25 1z"/></svg>
        (555) 014-1070 ext.201
      </li>
      <li>
        <svg viewBox="0 0 24 24" aria-hidden="true"><path d="M6.6 10.8a15.1 15.1 0 0 0 6.6 6.6l2.2-2.2a1 1 0 0 1 1-.25 11.4 11.4 0 0 0 3.6.57 1 1 0 0 1 1 1V20a1 1 0 0 1-1 1A17 17 0 0 1 3 4a1 1 0 0 1 1-1h3.5a1 1 0 0 1 1 1c0 1.25.2 2.45.57 3.6a1 1 0 0 1-.25 1z"/></svg>
        (555) 019-1069
      </li>
      <li>
        <svg viewBox="0 0 24 24" aria-hidden="true"><path d="M2 5h20v14H2zm2 2v.4l8 5.3 8-5.3V7zm0 2.8V17h16V9.8l-8 5.3z"/></svg>
        dvoronov@steadywave.example
      </li>
      <li>
        <svg viewBox="0 0 24 24" aria-hidden="true"><path d="M12 2a10 10 0 1 0 0 20 10 10 0 0 0 0-20zm6.9 6h-2.9a15 15 0 0 0-1.4-3.6A8 8 0 0 1 18.9 8zM12 4a13 13 0 0 1 1.9 4h-3.8A13 13 0 0 1 12 4zM4.3 14a8 8 0 0 1 0-4h3.4a16 16 0 0 0 0 4zm.8 2h2.9a15 15 0 0 0 1.4 3.6A8 8 0 0 1 5.1 16zM8 8H5.1a8 8 0 0 1 4.3-3.6A15 15 0 0 0 8 8zm4 12a13 13 0 0 1-1.9-4h3.8A13 13 0 0 1 12 20zm2.3-6H9.7a14 14 0 0 1 0-4h4.6a14 14 0 0 1 0 4zm.3 5.6A15 15 0 0 0 16 16h2.9a8 8 0 0 1-4.3 3.6zm1.7-5.6a16 16 0 0 0 0-4h3.4a8 8 0 0 1 0 4z"/></svg>
        www.steadywave.example
      </li>
    </ul>
  </div>
</section>

</body>
</html>
```